Tech Company PC Desktop Wallpaper

We need a graphic designer to come up with a PC desktop wallpaper to rollout to numerous computers managed by our business. We are a technology consultancy firm based in Perth, Western Australia that provides a number of IT services including datacentre/cloud services, software development, cyber security, managed services and more.

The vibe for this desktop wallpaper must be aligned with innovation, cutting edge, technology, cyber, revolutionary. When people see PC wallpaper it should scream "cutting edge" tech company.

With regards to the contents of the image, this is up to the designer however we would like to ask our logo to be featured in the design somewhere (we uploaded two different logo samples of different layout in vector format).

This wallpaper will go on numerous computers so we would like both 4:3 version as well as widescreen in the following dimensions:

4:3
1024 x 768
1440 x 1080
2048 x 1536

Widescreen:
HD: 1920 x 1080
UHD: 2560×1440
4K: 3840 x 2160
8K: 7680 x 4320

We will be using this wallpaper for both the Desktop Wallpaper and Windows 10 Lockscreen. Please be aware of the following items that will overlap the design by the Windows 10 operating system so be mindful of this when mapping out the design:
- Start Menu
- Desktop Icons that are generally on the LEFT of the screen
- Windows 10 Lockscreen has items on both the bottom left and right of the screen.

At the top right of the design we would like the following phone number and email address to be included so users have the support contact details:

Phone 08 9351 2046
Email support@bluequarrysystems.com.au

We are really looking forward to seeing the designs posted for this competition.

Target Market(s)

Information Technology

Requirements
Must have
• Must have our Logo, must scream cutting edge tech company
Should not have
• Be mindful of Windows 10 overlapping bits

```html
<!DOCTYPE html>
<html lang="en">
<head>
<meta charset="utf-8">
<title>Blue Quarry Systems Desktop Wallpaper</title>
<link rel="stylesheet" href="https://fonts.googleapis.com/css2?family=Saira:wght@400;600&display=swap">
<style>
  :root {
    --base-blue: #3794c5;
    --beam-light: #ffffff;
    --beam-teal: #b8ecea;
    --glow: #d6ecf2;
    --brand-ink: #97b3b8;
    --contact-ink: #f2fafc;
  }
  html, body {
    margin: 0;
    padding: 0;
    width: 1200px;
    height: 675px;
    overflow: hidden;
    background: var(--base-blue);
  }
  .wallpaper {
    position: relative;
    width: 1200px;
    height: 675px;
    overflow: hidden;
    background: var(--base-blue);
    font-family: "Saira", sans-serif;
  }
  .light-beams {
    position: absolute;
    inset: 0;
    width: 1200px;
    height: 675px;
  }
  .brand-name {
    position: absolute;
    left: 712px;
    top: 398px;
    margin: 0;
    font-family: "Saira", sans-serif;
    font-weight: 600;
    color: var(--brand-ink);
    text-transform: uppercase;
    line-height: 1;
    white-space: nowrap;
    transform: rotate(-13deg);
    transform-origin: 0 100%;
  }
  .brand-name .line-primary {
    display: block;
    font-size: 40px;
    letter-spacing: 0.5px;
  }
  .brand-name .line-secondary {
    display: block;
    font-size: 17px;
    letter-spacing: 31px;
    margin-top: 4px;
    padding-left: 3px;
  }
  .support-contact {
    position: absolute;
    top: 30px;
    right: 40px;
    margin: 0;
    color: var(--contact-ink);
    font-size: 14px;
    font-weight: 400;
    line-height: 1.7;
    text-align: right;
    font-style: normal;
  }
  .support-contact .contact-row {
    display: flex;
    align-items: center;
    justify-content: flex-end;
    gap: 8px;
  }
  .support-contact .contact-label {
    font-weight: 600;
    letter-spacing: 0.5px;
  }
  .support-contact svg {
    width: 14px;
    height: 14px;
    flex: none;
  }
</style>
</head>
<body>
  <main class="wallpaper">
    <svg class="light-beams" viewBox="0 0 1920 1080" preserveAspectRatio="none" aria-hidden="true">
      <defs>
        <radialGradient id="centre-glow" cx="960" cy="520" r="760" gradientUnits="userSpaceOnUse">
          <stop offset="0" stop-color="var(--glow)" stop-opacity="0.5"/>
          <stop offset="0.6" stop-color="var(--glow)" stop-opacity="0.1"/>
          <stop offset="1" stop-color="var(--glow)" stop-opacity="0"/>
        </radialGradient>
        <linearGradient id="beam-fade" x1="1150" y1="500" x2="1700" y2="300" gradientUnits="userSpaceOnUse">
          <stop offset="0" stop-color="var(--beam-light)" stop-opacity="0.45"/>
          <stop offset="1" stop-color="var(--beam-teal)" stop-opacity="0.35"/>
        </linearGradient>
      </defs>
      <rect class="backdrop" width="1920" height="1080" fill="var(--base-blue)"/>
      <polygon class="wide-beam" points="0,820 830,0 1920,0 1920,600 0,1040" fill="var(--beam-light)" opacity="0.16"/>
      <polygon class="narrow-beam" points="1213,0 1580,0 1830,1080 1010,1080" fill="url(#beam-fade)"/>
      <rect class="soft-glow" width="1920" height="1080" fill="url(#centre-glow)"/>
    </svg>

    <address class="support-contact">
      <span class="contact-row">
        <svg viewBox="0 0 24 24" aria-hidden="true"><path fill="currentColor" d="M6.6 10.8a15.1 15.1 0 0 0 6.6 6.6l2.2-2.2a1 1 0 0 1 1-.25 11.4 11.4 0 0 0 3.6.57 1 1 0 0 1 1 1V20a1 1 0 0 1-1 1A17 17 0 0 1 3 4a1 1 0 0 1 1-1h3.5a1 1 0 0 1 1 1c0 1.25.2 2.45.57 3.6a1 1 0 0 1-.25 1z"/></svg>
        <span class="contact-label">Phone</span> 08 9351 2046
      </span>
      <span class="contact-row">
        <svg viewBox="0 0 24 24" aria-hidden="true"><path fill="currentColor" d="M3 5h18a1 1 0 0 1 1 1v12a1 1 0 0 1-1 1H3a1 1 0 0 1-1-1V6a1 1 0 0 1 1-1zm9 7.2L4 7.3V17h16V7.3z"/></svg>
        <span class="contact-label">Email</span> support@bluequarrysystems.com.au
      </span>
    </address>

    <h1 class="brand-name">
      <span class="line-primary">Blue Quarry</span>
      <span class="line-secondary">Systems</span>
    </h1>
  </main>
</body>
</html>
```